Marlow Realty Real Estate Brokerage Recruiting Flyer

We are a real estate brokerage looking to hire more real estate agents. We need to list everything we have to offer as a company so real estate agents will join our company. this is our company website: www.Marlowrealty.example .

100% COMMISSION NO MONTHLY FEE
$450 Flat Transaction FEE

What We Offer:
24/7 Office Access
Free E & O Insurance for 1st Year
Free Online CE and PLE
Free 1,000 Business Cards
Free Professional Social Media Marketing
Free Printing, Scanning, and Copies
Free Buyer and Seller Presentation Packages
Free Filquay Cloud Based Document Management Access
Access to our Internal Brokerage Forum
Company Profit Sharing!
Private Offices Available to Rent

*Lead Generation Software with over 3,000 Leads
*10 Leads to Start
* Free Personal CRM and Website
*Restrictions and Rules apply

Company Address:
4817 Amberfield Road
Suite 512
Fairfax, VA 22194
Phone: 703-555-0147
email: info@marlowrealty.example

Target Market(s)

Real Estate Agents

Industry/Entity Type

Real Estate

Colors
0555a3
ffffff

Requirements
Must have
• 100% COMMISSION NO MONTHLY FEE
$450 Flat Transaction FEE

What We Offer:
24/7 Office Access
Free Online CE and PLE
Free 1,000 Business Cards
Company Profit Sharing!

*10 Leads to Start

Company Address:
4817 Amberfield Road
Suite 512
Fairfax, VA 22194
Phone: 703-555-0147

```html
<!DOCTYPE html>
<html lang="en">
<head>
<meta charset="utf-8">
<title>Marlow Realty – Agent Recruiting Flyer</title>
<link rel="stylesheet" href="https://fonts.googleapis.com/css2?family=Roboto:wght@400;500&family=Saira+Semi+Condensed:wght@600;700&display=swap">
<style>
  :root{
    --navy:#1b3b6f;
    --white:#ffffff;
    --stage:#ebebeb;
    --ink:#1a1a1a;
    --rule:#9aa8c0;
  }
  *{box-sizing:border-box;margin:0;padding:0}
  html,body{width:1200px;height:625px;overflow:hidden;background:var(--stage)}
  body{position:relative;font-family:"Roboto",Arial,sans-serif;color:var(--ink)}
  .sheet{position:absolute;width:414px;height:603px;background:var(--white)}
  .sheet--house{left:185px;top:13px}
  .sheet--couple{left:600px;top:9px;height:607px}
  .flyer{position:absolute;left:22px;top:20px;width:371px}
  .sheet--couple .flyer{left:21px;width:372px}

  .hero{position:relative;height:167px;overflow:hidden}
  .hero__photo{position:absolute;inset:0}
  .hero__photo--house{background:linear-gradient(180deg,#b8a6cf 0%,#d9b7c4 30%,#7d8fb2 60%,#3f4d6b 85%,#4f6b3f 100%)}
  .hero__photo--couple{background:linear-gradient(90deg,#c9cccf 0%,#d6d8da 45%,#9ea3a8 70%,#e7d5cf 100%)}
  .brand-box{position:absolute;background:var(--white);display:flex;align-items:center;justify-content:center;gap:6px}
  .sheet--house .brand-box{left:123px;bottom:0;width:137px;height:56px}
  .sheet--couple .brand-box{left:19px;top:1px;width:138px;height:56px}
  .brand-box__mark{width:14px;height:14px;background:var(--navy)}
  .brand-box__name{font-family:"Saira Semi Condensed",Arial,sans-serif;font-weight:600;font-size:17px;color:var(--navy);line-height:1;white-space:nowrap}

  .offer-banner{margin-top:3px;height:66px;background:var(--navy);padding:3px 10px 0}
  .offer-banner svg{display:block;width:351px;height:61px}
  .offer-banner text{font-family:"Saira Semi Condensed",Arial,sans-serif;font-weight:700;fill:var(--white)}

  .benefits{margin-top:3px;height:191px;border:1px solid var(--navy);border-top:none;position:relative}
  .benefits__title{font-weight:500;font-size:12.5px;color:var(--navy);line-height:12px;padding-left:2px;margin-top:-2px}
  .benefits__grid{display:grid;grid-template-columns:repeat(4,1fr);row-gap:8px;padding:5px 2px 0}
  .benefits__row3{display:flex;justify-content:center;gap:6px;padding:8px 40px 0 30px}
  .benefit{text-align:center;font-size:7.8px;line-height:10px;color:var(--ink)}
  .benefits__row3 .benefit{width:86px}
  .benefit svg{display:block;margin:0 auto 2px;width:24px;height:24px;fill:var(--navy)}

  .perks{display:grid;grid-template-columns:1fr 1fr;column-gap:8px;row-gap:8px;margin-top:3px}
  .perk{height:30px;background:var(--navy);border-radius:15px;display:flex;align-items:center;gap:6px;padding:0 4px;overflow:hidden}
  .perk--flip{flex-direction:row-reverse}
  .perk__star{flex:none;width:28px;height:28px;border-radius:50%;background:var(--white);border:3px solid var(--navy);
    box-shadow:0 0 0 1px var(--white);display:flex;align-items:center;justify-content:center;color:var(--navy);font-size:18px}
  .perk__text{flex:none;display:block;width:140px;height:24px}
  .perk__text text{font-family:"Saira Semi Condensed",Arial,sans-serif;font-weight:600;fill:var(--white)}

  .contact-bar{margin-top:4px;height:78px;background:var(--navy);color:var(--white);display:flex;padding:7px 8px 0}
  .contact-bar__address{width:181px;font-size:8.3px;line-height:11.7px;border-right:1px solid var(--white);height:64px;white-space:nowrap}
  .contact-bar__label{font-weight:500;text-decoration:underline;font-size:8.6px}
  .contact-line{display:flex;gap:5px;align-items:flex-start}
  .contact-line svg{flex:none;width:8px;height:8px;margin-top:2px;fill:var(--white)}
  .contact-line--cont{padding-left:13px}
  .contact-bar__license{padding-left:6px;font-family:"Saira Semi Condensed",Arial,sans-serif;font-weight:600;white-space:nowrap}
  .license__label{font-size:10px;line-height:11px}
  .license__states{font-size:12px;line-height:15px}
  .license__phone{display:inline-block;margin-top:5px;background:var(--white);color:var(--navy);border-radius:4px;font-size:16px;font-weight:700;line-height:18px;padding:0 4px}
</style>
</head>
<body>

<article class="sheet sheet--house">
  <div class="flyer">
    <header class="hero">
      <div class="hero__photo hero__photo--house" role="img" aria-label="Photo of a two-storey suburban house at dusk with lit windows"></div>
      <div class="brand-box"><span class="brand-box__mark"></span><span class="brand-box__name">Marlow Realty</span></div>
    </header>
    <section class="offer-banner">
      <svg viewBox="0 0 351 61" aria-label="100% commission no monthly fee, $450 flat transaction fee">
        <text x="3" y="23" font-size="22" textLength="345" lengthAdjust="spacingAndGlyphs">100% COMMISSION NO MONTHLY FEE</text>
        <rect x="0" y="29" width="351" height="1" fill="#9aa8c0"/>
        <text x="3" y="57" font-size="29" textLength="345" lengthAdjust="spacingAndGlyphs">$450 FLAT TRANSACTION FEE</text>
      </svg>
    </section>
    <section class="benefits">
      <h2 class="benefits__title">WHAT WE OFFER:</h2>
      <div class="benefits__grid">
        <div class="benefit"><svg viewBox="0 0 24 24"><path d="M12 2a10 10 0 1 0 0 20 10 10 0 0 0 0-20zm0 2.5a7.5 7.5 0 1 1 0 15 7.5 7.5 0 0 1 0-15z"/><rect x="11" y="7" width="2" height="6"/><rect x="11" y="11" width="5" height="2"/></svg>24/7 Office Access</div>
        <div class="benefit"><svg viewBox="0 0 24 24"><rect x="3" y="2" width="12" height="16" rx="1"/><path d="M15 11l6 2v4c0 3-3 5-6 6-3-1-5-3-5-6v-4z" fill="#fff"/><path d="M16 12l5 2v3c0 2.5-2.5 4.3-5 5-2.5-.7-4.5-2.5-4.5-5v-3z"/></svg>Free E &amp; O Insurance for 1st Year</div>
        <div class="benefit"><svg viewBox="0 0 24 24"><circle cx="6" cy="5" r="3"/><path d="M2 22v-9a4 4 0 0 1 8 0v9z"/><rect x="11" y="2" width="11" height="9" rx="1"/><rect x="15" y="11" width="2" height="9"/></svg>Free Online CE and PLE</div>
        <div class="benefit"><svg viewBox="0 0 24 24"><rect x="2" y="7" width="20" height="14" rx="2"/><rect x="6" y="3" width="14" height="4" rx="1"/><circle cx="8" cy="13" r="2" fill="#fff"/><rect x="12" y="12" width="7" height="1.6" fill="#fff"/><rect x="12" y="15" width="7" height="1.6" fill="#fff"/></svg>Free 1,000 Business Cards</div>
        <div class="benefit"><svg viewBox="0 0 24 24"><path d="M3 10h4l9-5v14l-9-5H3z"/><rect x="5" y="14" width="3" height="6"/><circle cx="19" cy="4" r="2"/><circle cx="20" cy="12" r="2"/><circle cx="19" cy="20" r="2"/></svg>Free Professional Social Media Marketing</div>
        <div class="benefit"><svg viewBox="0 0 24 24"><rect x="6" y="2" width="12" height="6"/><rect x="2" y="8" width="20" height="10" rx="2"/><rect x="6" y="14" width="12" height="8" fill="#fff" stroke="#1b3b6f" stroke-width="2"/></svg>Free Printing, Scanning, and Copies</div>
        <div class="benefit"><svg viewBox="0 0 24 24"><path d="M12 2l9 4v10l-9 5-9-5V6z"/><rect x="16" y="12" width="6" height="10" fill="#fff" stroke="#1b3b6f" stroke-width="1.6"/></svg>Free Buyer and Seller Presentation Packages</div>
        <div class="benefit"><svg viewBox="0 0 24 24"><path d="M7 11a5 5 0 0 1 10-1 3.5 3.5 0 0 1 0 7H6a3 3 0 0 1 1-6z"/><rect x="11" y="17" width="2" height="3"/><rect x="4" y="19" width="16" height="2"/><rect x="3" y="20" width="4" height="3"/><rect x="17" y="20" width="4" height="3"/></svg>Free Filquay Cloud Based Document Management Access</div>
      </div>
      <div class="benefits__row3">
        <div class="benefit"><svg viewBox="0 0 24 24"><rect x="3" y="1" width="18" height="7" rx="2"/><circle cx="12" cy="12" r="2.5"/><circle cx="5" cy="13" r="2"/><circle cx="19" cy="13" r="2"/><path d="M8 22a4 4 0 0 1 8 0zM1 22a4 4 0 0 1 7-1v1zM23 22a4 4 0 0 0-7-1v1z"/></svg>Access to our Internal Brokerage Forum Company Profit Sharing!</div>
        <div class="benefit"><svg viewBox="0 0 24 24"><circle cx="16" cy="6" r="5"/><rect x="1" y="14" width="5" height="8"/><path d="M6 15h6l3 2h5a2 2 0 0 1 0 3H6z"/></svg>Company Profit Shar-ing!</div>
        <div class="benefit"><svg viewBox="0 0 24 24"><rect x="2" y="10" width="5" height="12"/><rect x="8" y="4" width="6" height="18"/><rect x="15" y="12" width="5" height="10"/><circle cx="19" cy="6" r="3.5"/></svg>Private Offices Availa-ble to Rent</div>
      </div>
    </section>
    <section class="perks">
      <div class="perk"><span class="perk__star">*</span>
        <svg class="perk__text" viewBox="0 0 140 24"><text x="0" y="10" font-size="10" textLength="136" lengthAdjust="spacingAndGlyphs">LEAD GENERATION SOFTWARE</text><text x="0" y="21" font-size="10" textLength="122" lengthAdjust="spacingAndGlyphs">WITH OVER 3,000 LEADS</text></svg></div>
      <div class="perk"><span class="perk__star">*</span>
        <svg class="perk__text" viewBox="0 0 140 24"><text x="0" y="10" font-size="11" textLength="108" lengthAdjust="spacingAndGlyphs">FREE PERSONAL CRM</text><text x="0" y="21" font-size="11" textLength="72" lengthAdjust="spacingAndGlyphs">AND WEBSITE</text></svg></div>
      <div class="perk perk--flip"><span class="perk__star">*</span>
        <svg class="perk__text" viewBox="0 0 140 24"><text x="74" y="16" font-size="11.5" text-anchor="middle" textLength="104" lengthAdjust="spacingAndGlyphs">10 LEADS TO START</text></svg></div>
      <div class="perk perk--flip"><span class="perk__star">*</span>
        <svg class="perk__text" viewBox="0 0 140 24"><text x="138" y="10" font-size="11" text-anchor="end" textLength="104" lengthAdjust="spacingAndGlyphs">RESTRICTIONS AND</text><text x="138" y="21" font-size="11" text-anchor="end" textLength="70" lengthAdjust="spacingAndGlyphs">RULES APPLY</text></svg></div>
    </section>
    <footer class="contact-bar">
      <div class="contact-bar__address">
        <p class="contact-bar__label">COMPANY ADDRESS</p>
        <p class="contact-line"><svg viewBox="0 0 10 10"><rect x="1" y="2" width="8" height="8"/></svg>4817 Amberfield Road, Suite 512</p>
        <p class="contact-line contact-line--cont">Fairfax, VA 22194</p>
        <p class="contact-line"><svg viewBox="0 0 10 10"><circle cx="5" cy="3" r="2.5"/><path d="M0 10a5 4 0 0 1 10 0z"/></svg>703-555-0147</p>
        <p class="contact-line"><svg viewBox="0 0 10 10"><rect x="0" y="2" width="10" height="7"/></svg>info@marlowrealty.example</p>
      </div>
      <div class="contact-bar__license">
        <p class="license__label">LICENSED IN</p>
        <p class="license__states">D.C &nbsp;|&nbsp; MARYLAND | VIRGINIA</p>
        <p class="license__phone">703-555-0147</p>
      </div>
    </footer>
  </div>
</article>

<article class="sheet sheet--couple">
  <div class="flyer">
    <header class="hero">
      <div class="hero__photo hero__photo--couple" role="img" aria-label="Photo of a smiling couple holding house keys and a small model home"></div>
      <div class="brand-box"><span class="brand-box__mark"></span><span class="brand-box__name">Marlow Realty</span></div>
    </header>
    <section class="offer-banner">
      <svg viewBox="0 0 351 61" aria-label="100% commission no monthly fee, $450 flat transaction fee">
        <text x="3" y="23" font-size="22" textLength="345" lengthAdjust="spacingAndGlyphs">100% COMMISSION NO MONTHLY FEE</text>
        <rect x="0" y="29" width="351" height="1" fill="#9aa8c0"/>
        <text x="3" y="57" font-size="29" textLength="345" lengthAdjust="spacingAndGlyphs">$450 FLAT TRANSACTION FEE</text>
      </svg>
    </section>
    <section class="benefits">
      <h2 class="benefits__title">WHAT WE OFFER:</h2>
      <div class="benefits__grid">
        <div class="benefit"><svg viewBox="0 0 24 24"><path d="M12 2a10 10 0 1 0 0 20 10 10 0 0 0 0-20zm0 2.5a7.5 7.5 0 1 1 0 15 7.5 7.5 0 0 1 0-15z"/><rect x="11" y="7" width="2" height="6"/><rect x="11" y="11" width="5" height="2"/></svg>24/7 Office Access</div>
        <div class="benefit"><svg viewBox="0 0 24 24"><rect x="3" y="2" width="12" height="16" rx="1"/><path d="M15 11l6 2v4c0 3-3 5-6 6-3-1-5-3-5-6v-4z" fill="#fff"/><path d="M16 12l5 2v3c0 2.5-2.5 4.3-5 5-2.5-.7-4.5-2.5-4.5-5v-3z"/></svg>Free E &amp; O Insurance for 1st Year</div>
        <div class="benefit"><svg viewBox="0 0 24 24"><circle cx="6" cy="5" r="3"/><path d="M2 22v-9a4 4 0 0 1 8 0v9z"/><rect x="11" y="2" width="11" height="9" rx="1"/><rect x="15" y="11" width="2" height="9"/></svg>Free Online CE and PLE</div>
        <div class="benefit"><svg viewBox="0 0 24 24"><rect x="2" y="7" width="20" height="14" rx="2"/><rect x="6" y="3" width="14" height="4" rx="1"/><circle cx="8" cy="13" r="2" fill="#fff"/><rect x="12" y="12" width="7" height="1.6" fill="#fff"/><rect x="12" y="15" width="7" height="1.6" fill="#fff"/></svg>Free 1,000 Business Cards</div>
        <div class="benefit"><svg viewBox="0 0 24 24"><path d="M3 10h4l9-5v14l-9-5H3z"/><rect x="5" y="14" width="3" height="6"/><circle cx="19" cy="4" r="2"/><circle cx="20" cy="12" r="2"/><circle cx="19" cy="20" r="2"/></svg>Free Professional Social Media Marketing</div>
        <div class="benefit"><svg viewBox="0 0 24 24"><rect x="6" y="2" width="12" height="6"/><rect x="2" y="8" width="20" height="10" rx="2"/><rect x="6" y="14" width="12" height="8" fill="#fff" stroke="#1b3b6f" stroke-width="2"/></svg>Free Printing, Scanning, and Copies</div>
        <div class="benefit"><svg viewBox="0 0 24 24"><path d="M12 2l9 4v10l-9 5-9-5V6z"/><rect x="16" y="12" width="6" height="10" fill="#fff" stroke="#1b3b6f" stroke-width="1.6"/></svg>Free Buyer and Seller Presentation Packages</div>
        <div class="benefit"><svg viewBox="0 0 24 24"><path d="M7 11a5 5 0 0 1 10-1 3.5 3.5 0 0 1 0 7H6a3 3 0 0 1 1-6z"/><rect x="11" y="17" width="2" height="3"/><rect x="4" y="19" width="16" height="2"/><rect x="3" y="20" width="4" height="3"/><rect x="17" y="20" width="4" height="3"/></svg>Free Filquay Cloud Based Document Management Access</div>
      </div>
      <div class="benefits__row3">
        <div class="benefit"><svg viewBox="0 0 24 24"><rect x="3" y="1" width="18" height="7" rx="2"/><circle cx="12" cy="12" r="2.5"/><circle cx="5" cy="13" r="2"/><circle cx="19" cy="13" r="2"/><path d="M8 22a4 4 0 0 1 8 0zM1 22a4 4 0 0 1 7-1v1zM23 22a4 4 0 0 0-7-1v1z"/></svg>Access to our Internal Brokerage Forum Company Profit Sharing!</div>
        <div class="benefit"><svg viewBox="0 0 24 24"><circle cx="16" cy="6" r="5"/><rect x="1" y="14" width="5" height="8"/><path d="M6 15h6l3 2h5a2 2 0 0 1 0 3H6z"/></svg>Company Profit Shar-ing!</div>
        <div class="benefit"><svg viewBox="0 0 24 24"><rect x="2" y="10" width="5" height="12"/><rect x="8" y="4" width="6" height="18"/><rect x="15" y="12" width="5" height="10"/><circle cx="19" cy="6" r="3.5"/></svg>Private Offices Availa-ble to Rent</div>
      </div>
    </section>
    <section class="perks">
      <div class="perk"><span class="perk__star">*</span>
        <svg class="perk__text" viewBox="0 0 140 24"><text x="0" y="10" font-size="10" textLength="136" lengthAdjust="spacingAndGlyphs">LEAD GENERATION SOFTWARE</text><text x="0" y="21" font-size="10" textLength="122" lengthAdjust="spacingAndGlyphs">WITH OVER 3,000 LEADS</text></svg></div>
      <div class="perk"><span class="perk__star">*</span>
        <svg class="perk__text" viewBox="0 0 140 24"><text x="0" y="10" font-size="11" textLength="108" lengthAdjust="spacingAndGlyphs">FREE PERSONAL CRM</text><text x="0" y="21" font-size="11" textLength="72" lengthAdjust="spacingAndGlyphs">AND WEBSITE</text></svg></div>
      <div class="perk perk--flip"><span class="perk__star">*</span>
        <svg class="perk__text" viewBox="0 0 140 24"><text x="74" y="16" font-size="11.5" text-anchor="middle" textLength="104" lengthAdjust="spacingAndGlyphs">10 LEADS TO START</text></svg></div>
      <div class="perk perk--flip"><span class="perk__star">*</span>
        <svg class="perk__text" viewBox="0 0 140 24"><text x="138" y="10" font-size="11" text-anchor="end" textLength="104" lengthAdjust="spacingAndGlyphs">RESTRICTIONS AND</text><text x="138" y="21" font-size="11" text-anchor="end" textLength="70" lengthAdjust="spacingAndGlyphs">RULES APPLY</text></svg></div>
    </section>
    <footer class="contact-bar">
      <div class="contact-bar__address">
        <p class="contact-bar__label">COMPANY ADDRESS</p>
        <p class="contact-line"><svg viewBox="0 0 10 10"><rect x="1" y="2" width="8" height="8"/></svg>4817 Amberfield Road, Suite 512</p>
        <p class="contact-line contact-line--cont">Fairfax, VA 22194</p>
        <p class="contact-line"><svg viewBox="0 0 10 10"><circle cx="5" cy="3" r="2.5"/><path d="M0 10a5 4 0 0 1 10 0z"/></svg>703-555-0147</p>
        <p class="contact-line"><svg viewBox="0 0 10 10"><rect x="0" y="2" width="10" height="7"/></svg>info@marlowrealty.example</p>
      </div>
      <div class="contact-bar__license">
        <p class="license__label">LICENSED IN</p>
        <p class="license__states">D.C &nbsp;|&nbsp; MARYLAND | VIRGINIA</p>
        <p class="license__phone">703-555-0147</p>
      </div>
    </footer>
  </div>
</article>

</body>
</html>
```